Business Cards

Business cards (double-sided) to be handed out to clients and potential clients, with contact details, logo .

Target Market(s)

Small to medium size businesses

Industry/Entity Type

Accountants

Contact Information for Business Card

Brightwater Ledger & Counsel Ltd

Colors

Designer to choose only greyscale colors for use in the design.

Requirements
Must have
• Name, Title, Address, Phone number, Email, Website
Nice to have
• Modern, clean lines, classy
Should not have
• Business cards to be double-sided. Form keeps reverting to single-sided.

```html
<!DOCTYPE html>
<html lang="en">
<head>
<meta charset="utf-8">
<title>Brightwater Ledger &amp; Counsel – Business Cards</title>
<link href="https://fonts.googleapis.com/css2?family=Montserrat:wght@400;500;700&display=swap" rel="stylesheet">
<style>
  :root {
    --backdrop: #2e2e2e;
    --card-light: #ffffff;
    --card-dark: #151515;
    --ink: #1a1a1a;
    --ink-soft: #6e6e6e;
    --paper-text: #f4f4f4;
  }
  * { box-sizing: border-box; margin: 0; padding: 0; }
  html, body {
    width: 1200px; height: 1200px; overflow: hidden;
    background: var(--backdrop);
    font-family: "Montserrat", sans-serif;
  }
  .sheet {
    width: 1200px; height: 1200px;
    display: flex; flex-direction: column; align-items: center; justify-content: center;
    gap: 60px;
  }
  .card {
    position: relative;
    width: 840px; height: 480px;
    border-radius: 36px;
    box-shadow: 0 18px 40px rgba(0,0,0,.45);
  }
  .card--front { background: var(--card-light); color: var(--ink); }
  .card--back {
    background: linear-gradient(135deg, #1c1c1c 0%, var(--card-dark) 60%, #101010 100%);
    color: var(--paper-text);
    display: flex; align-items: center; justify-content: center;
  }

  .brand {
    display: flex; align-items: center; gap: 16px;
    font-weight: 500; text-transform: uppercase; letter-spacing: .14em; line-height: 1.25;
  }
  .brand__square { width: 14px; height: 14px; background: currentColor; flex: none; }
  .card--front .brand { position: absolute; right: 70px; top: 110px; font-size: 22px; }
  .card--back .brand { font-size: 34px; }

  .person {
    position: absolute; left: 80px; top: 225px;
  }
  .person__header {
    border-left: 5px solid var(--ink);
    padding-left: 14px;
    margin-bottom: 22px;
  }
  .person__name { font-size: 36px; font-weight: 700; letter-spacing: .02em; line-height: 1.05; }
  .person__title { font-size: 17px; font-weight: 400; color: var(--ink-soft); letter-spacing: .03em; margin-top: 4px; }

  .contact-list { list-style: none; padding-left: 4px; }
  .contact-list li {
    display: flex; align-items: flex-start; gap: 12px;
    font-size: 16px; font-weight: 500; line-height: 1.35; margin-bottom: 6px;
  }
  .contact-list svg { width: 18px; height: 18px; flex: none; margin-top: 1px; fill: var(--ink); }
</style>
</head>
<body>
<main class="sheet">

  <section class="card card--front" aria-label="Business card front">
    <div class="brand">
      <span class="brand__square"></span>
      <span>Brightwater<br>Ledger &amp; Counsel</span>
    </div>

    <div class="person">
      <div class="person__header">
        <h1 class="person__name">JOHN DOE</h1>
        <p class="person__title">CEO | FOUNDER</p>
      </div>
      <ul class="contact-list">
        <li>
          <svg viewBox="0 0 24 24" aria-hidden="true"><path d="M6.6 10.8a15.1 15.1 0 0 0 6.6 6.6l2.2-2.2a1 1 0 0 1 1-.25 11.4 11.4 0 0 0 3.6.57 1 1 0 0 1 1 1V20a1 1 0 0 1-1 1A17 17 0 0 1 3 4a1 1 0 0 1 1-1h3.5a1 1 0 0 1 1 1c0 1.25.2 2.45.57 3.57a1 1 0 0 1-.25 1z"/></svg>
          <span>(000) 000 0000</span>
        </li>
        <li>
          <svg viewBox="0 0 24 24" aria-hidden="true"><path d="M2 5h20v14H2z M4 7v.5l8 5 8-5V7l-8 5z" fill-rule="evenodd"/></svg>
          <span>email@youremail.com</span>
        </li>
        <li>
          <svg viewBox="0 0 24 24" aria-hidden="true"><path d="M12 2a10 10 0 1 0 0 20 10 10 0 0 0 0-20zm6.9 6h-3a15 15 0 0 0-1.3-3.9A8 8 0 0 1 18.9 8zM12 4c.9 1.2 1.6 2.6 2 4h-4c.4-1.4 1.1-2.8 2-4zM4.3 14a8 8 0 0 1 0-4h3.4a16 16 0 0 0 0 4zm.8 2h3a15 15 0 0 0 1.3 3.9A8 8 0 0 1 5.1 16zm3-8h-3a8 8 0 0 1 4.3-3.9A15 15 0 0 0 8.1 8zM12 20c-.9-1.2-1.6-2.6-2-4h4c-.4 1.4-1.1 2.8-2 4zm2.3-6H9.7a14 14 0 0 1 0-4h4.6a14 14 0 0 1 0 4zm.3 5.9a15 15 0 0 0 1.3-3.9h3a8 8 0 0 1-4.3 3.9zm1.7-5.9a16 16 0 0 0 0-4h3.4a8 8 0 0 1 0 4z"/></svg>
          <span>www.yourwebsite.com</span>
        </li>
        <li>
          <svg viewBox="0 0 24 24" aria-hidden="true"><path d="M12 2a7 7 0 0 0-7 7c0 5.2 7 13 7 13s7-7.8 7-13a7 7 0 0 0-7-7zm0 9.5A2.5 2.5 0 1 1 12 6.5a2.5 2.5 0 0 1 0 5z"/></svg>
          <span>Street Address City, State<br>Zip Code 0000 000 Country</span>
        </li>
      </ul>
    </div>
  </section>

  <section class="card card--back" aria-label="Business card back">
    <div class="brand">
      <span class="brand__square"></span>
      <span>Brightwater<br>Ledger &amp; Counsel</span>
    </div>
  </section>

</main>
</body>
</html>
```